Business Card Design Project

Company name will be Tolvan Crest (named after my black lab and his fraying muzzle) Business is in the body armor, Security product industry servicing the state, local, and federal law enforcement markets. I want a more formal and serious logo for both business cards and letterhead

```html
<!DOCTYPE html>
<html lang="en">
<head>
<meta charset="utf-8">
<title>Tolvan Crest — Business Card</title>
<link href="https://fonts.googleapis.com/css2?family=Old+Standard+TT:wght@400;700&display=swap" rel="stylesheet">
<style>
  :root {
    --backdrop: #e8e5e1;
    --front-light: #f4f4f4;
    --front-mid: #9a9a9a;
    --front-dark: #3a3a3a;
    --card-white: #ffffff;
    --ink: #111111;
    --ink-soft: #2a2a2a;
    --brand-navy: #2f3f66;
    --divider: #1c1c1c;
  }
  * { box-sizing: border-box; margin: 0; padding: 0; }
  html, body {
    width: 1200px;
    height: 1000px;
    overflow: hidden;
    background: var(--backdrop);
  }
  .canvas {
    position: relative;
    width: 1200px;
    height: 1000px;
    font-family: "Old Standard TT", Georgia, serif;
  }
  .card {
    position: absolute;
    box-shadow: 0 2px 6px rgba(0,0,0,0.18);
  }
  .card-front {
    left: 48px;
    top: 18px;
    width: 680px;
    height: 452px;
    background: radial-gradient(ellipse 60% 62% at 50% 42%, var(--front-light) 0%, var(--front-mid) 55%, var(--front-dark) 100%);
    display: flex;
    align-items: center;
    justify-content: center;
  }
  .brand-lockup {
    display: flex;
    align-items: center;
    gap: 16px;
    color: var(--brand-navy);
    font-weight: 700;
  }
  .brand-mark {
    width: 22px;
    height: 22px;
    border-radius: 50%;
    background: var(--brand-navy);
  }
  .card-front .brand-name { font-size: 54px; letter-spacing: 1px; }
  .card-back {
    left: 455px;
    top: 518px;
    width: 676px;
    height: 450px;
    background: var(--card-white);
  }
  .back-logo {
    position: absolute;
    left: 0;
    top: 0;
    width: 318px;
    height: 100%;
    display: flex;
    align-items: center;
    justify-content: center;
    padding-bottom: 70px;
  }
  .back-logo .brand-lockup { gap: 9px; }
  .back-logo .brand-mark { width: 12px; height: 12px; }
  .back-logo .brand-name { font-size: 27px; }
  .divider {
    position: absolute;
    left: 317px;
    top: 100px;
    width: 2px;
    height: 245px;
    background: linear-gradient(to bottom, rgba(28,28,28,0), var(--divider) 20%, var(--divider) 80%, rgba(28,28,28,0));
  }
  .contact-block {
    position: absolute;
    left: 365px;
    top: 134px;
    color: var(--ink);
  }
  .person-name {
    font-size: 31px;
    font-weight: 400;
    margin-left: 22px;
    line-height: 1.1;
  }
  .person-title {
    font-size: 16px;
    font-weight: 700;
    color: var(--ink-soft);
    margin-top: 8px;
  }
  .contact-list {
    list-style: none;
    margin-top: 34px;
  }
  .contact-list li {
    display: flex;
    align-items: flex-start;
    gap: 14px;
    font-size: 12px;
    font-weight: 700;
    line-height: 1.15;
    margin-bottom: 9px;
  }
  .contact-list li.email { font-size: 14px; font-weight: 400; }
  .contact-list svg { width: 20px; height: 18px; flex: none; }
</style>
</head>
<body>
<main class="canvas">
  <section class="card card-front" aria-label="Card front">
    <div class="brand-lockup">
      <span class="brand-mark"></span>
      <span class="brand-name">Tolvan Crest</span>
    </div>
  </section>

  <section class="card card-back" aria-label="Card back">
    <div class="back-logo">
      <div class="brand-lockup">
        <span class="brand-mark"></span>
        <span class="brand-name">Tolvan Crest</span>
      </div>
    </div>
    <div class="divider"></div>
    <div class="contact-block">
      <h1 class="person-name">Marek Ostrow</h1>
      <p class="person-title">Manufacturers Rep Principal</p>
      <ul class="contact-list">
        <li>
          <svg viewBox="0 0 20 18" aria-hidden="true"><path d="M10 1 L19 9 H16 V17 H12 V12 H8 V17 H4 V9 H1 Z" fill="#111"/></svg>
          <span>4107 Harbor Lane East<br>Coral Point, FL 32199</span>
        </li>
        <li>
          <svg viewBox="0 0 20 18" aria-hidden="true"><rect x="6" y="1" width="9" height="16" rx="1.5" fill="none" stroke="#111" stroke-width="1.6"/><rect x="8" y="4" width="5" height="4" fill="#111"/><circle cx="10.5" cy="13" r="1.2" fill="#111"/></svg>
          <span>555-014-2763</span>
        </li>
        <li class="email">
          <svg viewBox="0 0 20 18" aria-hidden="true"><rect x="4" y="4" width="14" height="10" fill="none" stroke="#111" stroke-width="1.3"/><path d="M4 4 L11 10 L18 4" fill="none" stroke="#111" stroke-width="1.3"/><path d="M0 8 H3 M1 11 H3" stroke="#111" stroke-width="1"/></svg>
          <span>mostrow@tolvancrest.com</span>
        </li>
      </ul>
    </div>
  </section>
</main>
</body>
</html>
```